Upscale business cards needed for family business

We need professional business cards created for several family members. We are a family business holding company. We would like these relatively simple and straightforward, but also with a unique element to set them apart. Probably stick with neutral and simple colors - white, grey etc. We need space for the traditional elements, including name, title, address, email/phone number. And we will be creating several from this template so it needs to be template that is easy to switch information in and out of.

Industry/Entity Type

Business

Contact Information for Business Card

Please include the attached Dunmore Ventures logo.

Requirements
Must have
• The attached Dunmore Ventures logo.

```html
<!DOCTYPE html>
<html lang="en">
<head>
<meta charset="utf-8">
<title>Dunmore Ventures – Business Cards</title>
<link rel="stylesheet" href="https://fonts.googleapis.com/css2?family=Cinzel:wght@400;600&family=Lato:wght@400;700&display=swap">
<style>
  :root {
    --bg: #3a3a3b;
    --card-dark: #242323;
    --card-light: #ffffff;
    --gold: #d4a22e;
    --ink: #2a2a2a;
    --text-light: #f2f2f2;
  }
  * { margin: 0; padding: 0; box-sizing: border-box; }
  html, body { width: 1200px; height: 810px; overflow: hidden; background: var(--bg); }
  .canvas { position: relative; width: 1200px; height: 810px; }

  .card {
    position: absolute;
    width: 560px;
    height: 320px;
    border-radius: 22px;
    overflow: hidden;
    box-shadow: 0 14px 30px rgba(0,0,0,0.35);
  }
  .card--back { left: 50px; top: 80px; background: var(--card-dark); }
  .card--front { left: 590px; top: 410px; background: var(--card-light); }

  .brand {
    font-family: "Cinzel", serif;
    font-weight: 600;
    letter-spacing: 0.06em;
    text-align: center;
    text-transform: uppercase;
  }
  .card--back .brand {
    position: absolute; left: 0; right: 0; top: 118px;
    font-size: 30px; color: var(--text-light); line-height: 1.1;
  }
  .brand-suffix { display: block; font-size: 14px; letter-spacing: 0.3em; margin-top: 4px; }
  .card--back .website {
    position: absolute; left: 0; right: 0; top: 220px;
    font-family: "Lato", sans-serif; font-size: 14px; color: var(--gold);
    text-align: center;
  }

  .front-shape { position: absolute; inset: 0; width: 560px; height: 320px; }
  .card--front .brand {
    position: absolute; left: 40px; top: 56px; width: 330px;
    font-size: 26px; color: var(--ink); line-height: 1.1;
  }
  .holder {
    position: absolute; right: 26px; top: 136px;
    text-align right; text-align: right; font-family: "Lato", sans-serif; color: var(--text-light);
  }
  .holder-name {
    font-family: "Cinzel", serif; font-weight: 600; font-size: 20px;
    color: var(--gold); letter-spacing: 0.04em; margin-bottom: 4px;
  }
  .holder-title { font-size: 13px; margin-bottom: 12px; }
  .holder-address { font-size: 13px; line-height: 1.45; }

  .contacts {
    position: absolute; left: 158px; top: 222px; list-style: none;
    font-family: "Lato", sans-serif; font-size: 13px; color: var(--text-light);
  }
  .contacts li { display: flex; align-items: center; gap: 9px; height: 22px; }
  .contacts svg { width: 13px; height: 13px; fill: none; stroke: var(--gold); stroke-width: 1.6; flex: none; }
</style>
</head>
<body>
<main class="canvas">

  <section class="card card--back" aria-label="Card back">
    <div class="brand">Dunmore Ventures<span class="brand-suffix">Inc</span></div>
    <p class="website">www.dunmoreventuresinc.com</p>
  </section>

  <section class="card card--front" aria-label="Card front">
    <svg class="front-shape" viewBox="0 0 560 320" aria-hidden="true">
      <path d="M30 320 C80 190 240 104 560 84 L560 100 C250 120 100 200 50 320 Z" fill="var(--gold)"/>
      <path d="M50 320 C100 200 250 120 560 100 L560 320 Z" fill="var(--card-dark)"/>
    </svg>

    <div class="brand">Dunmore Ventures<span class="brand-suffix">Inc</span></div>

    <div class="holder">
      <p class="holder-name">Daniel Avery</p>
      <p class="holder-title">President @ CEO</p>
      <p class="holder-address">Suite 210, Larkspur Row<br>Harbor Falls, USA 90411</p>
    </div>

    <ul class="contacts">
      <li><svg viewBox="0 0 14 14"><path d="M3 1.5l2 2.5-1 1.5c.8 1.8 2 3 3.8 3.8l1.5-1 2.5 2-1 2C6 12 2 8 1 3.5z"/></svg>(000) 000 0000</li>
      <li><svg viewBox="0 0 14 14"><rect x="4" y="1" width="6" height="12" rx="1"/><path d="M6.3 11h1.4"/></svg>(000) 000 0000</li>
      <li><svg viewBox="0 0 14 14"><rect x="1" y="3" width="12" height="8"/><path d="M1 3l6 5 6-5"/></svg>info@dunmoreventuresinc.com</li>
      <li><svg viewBox="0 0 14 14"><circle cx="7" cy="7" r="5.5"/><path d="M1.5 7h11M7 1.5c-2.5 3-2.5 8 0 11M7 1.5c2.5 3 2.5 8 0 11"/></svg>www.dunmoreventuresinc.com</li>
    </ul>
  </section>

</main>
</body>
</html>
```